依頼詳細
現行のホームページがかなり以前のものになりますので、今回の
リニューアルを機に、デザインの刷新を希望しております。

かしこまりすぎず、先鋭的で、現代的なデザインを希望しております。
動線が明確で、ユーザーが迷子にならないようなものを希望しております。
あくまでイメージとしての簡潔なワイヤーフレームを添付しておりますが、
ランサー様の自由なご発想によるデザインを期待しております。

デザインの参考にして頂きたいサイトを共有いたしますのでご確認ください。

https://www.minatoseiki.jp/
上記サイトのようなお知らせの表示を希望します。

https://haruden-na.com/
グループ支社となります。MVは動画も検討しております。

https://haruden.co.kr/

https://www.valmerco.com/
色味・構成が希望に近いです。

https://www.tqr-inc.co.jp/
コンテンツ配置が希望と似ております。

※その他詳細内容はTOPデザイン要望書と下記添付ファイルをご確認ください。
パスワードは補足説明内に記載しております。
https://filevaultex.com/download/a7e21f90bd3c44d8a2c6f05e18b7d2c94e61f03a
青系、水色系
• イラストレーター形式 (.ai)
• フォトショップ形式 (.psd)
■写真・データ(添付ファイル内) パスワード:qmd384527
Pixmora Stock [ https://stock.pixmora-example.com/jp/ ] で定期契約をしています。
また定期契約のものは弊社の負担となり、ランサー様に負担はありません。
カンプ画像を入れてください。その際、通常アセットで購入できる画像でお願いいたします。

■サイトマップ・ワイヤーフレーム(添付ファイル内)
デザイナー様で一案感じられる箇所がございましたら、ご提案いただければ幸いです。

■文章について
ワイヤーフレーム内に記載されているテキストを使用してください。
可能な限り「ダミーテキスト」を繰り返した表記は避けていただけますと幸いです。

■フォントについて
・WEB上で使用可能な無料のフォントで作成お願い致します。
・OSに紐づくフォントの使用は控えていただければと思います 。(ヒラギノなど)

■サイズについて
TOPデザイン自体の画像サイズは、横幅1300pxで提案をお願いできればと思います。(縦幅の制限はございません)

※通常業務へ支障をきたす為、当企業へのお問い合わせはお控え下さい。
皆様ご提案くださりありがとうございます。
様々なパターンで検討させていただきたいので、期限を延長させていただきます。
ワイヤーフレーム通りではなく、自由なご発想でのご提案もお待ちしております。
皆様ご提案くださりありがとうございます。
様々なバリエーションで検討させていただきたい為、
期限いっぱいまで延長とさせていただきます。

```html
<!DOCTYPE html>
<html lang="ja">
<head>
<meta charset="utf-8">
<title>HARUDEN | LIVING WITH HYDRAULIC</title>
<link href="https://fonts.googleapis.com/css2?family=Montserrat:wght@400;600;700&family=Noto+Sans+JP:wght@400;500;700&display=swap" rel="stylesheet">
<style>
:root{
  --navy:#0c2a5b;
  --blue:#1a5aa8;
  --sky:#2f8fd6;
  --dark:#2b2f36;
  --darker:#1e2126;
  --line:#e1e5ea;
  --text:#333;
  --muted:#888;
  --pale:#f3f6f9;
}
*{box-sizing:border-box;margin:0;padding:0}
html,body{width:1200px;height:3120px;overflow:hidden}
body{font-family:"Noto Sans JP",sans-serif;color:var(--text);background:#fff;position:relative;font-size:13px}
.en{font-family:"Montserrat",sans-serif}
a{color:inherit;text-decoration:none}

/* header */
.site-header{position:absolute;top:0;left:0;width:1200px;height:88px;display:flex;align-items:center;padding:0 40px;background:#fff}
.brand{font-family:"Montserrat",sans-serif;font-weight:700;font-size:28px;color:var(--blue);letter-spacing:1px}
.header-right{margin-left:auto;display:flex;flex-direction:column;align-items:flex-end;gap:12px}
.utility{display:flex;gap:12px;font-size:11px;color:var(--muted);align-items:center}
.search{width:110px;height:18px;border:1px solid var(--line);border-radius:2px}
.global-nav{display:flex;font-size:12px}
.global-nav a{padding:0 14px;border-left:1px solid var(--line)}
.global-nav a:first-child{border-left:none;color:var(--blue);font-weight:700}

/* hero */
.hero{position:absolute;top:88px;left:0;width:1200px;height:416px;background:
  radial-gradient(ellipse 420px 160px at 70% 78%,#6f5d45 0%,transparent 70%),
  linear-gradient(180deg,#d6e2ee 0%,#eef2f5 42%,#c2ae92 66%,#8c7a62 100%)}
.hero-copy{position:absolute;left:110px;top:120px}
.hero-copy h1{font-family:"Montserrat",sans-serif;font-weight:700;font-size:40px;color:var(--navy);letter-spacing:1px}
.hero-copy p{font-size:14px;color:var(--navy);margin-top:6px;font-weight:500}
.hero-arrow{position:absolute;top:193px;width:20px;height:30px}
.dots{position:absolute;top:512px;left:0;width:1200px;display:flex;justify-content:center;gap:10px}
.dots span{width:8px;height:8px;border-radius:50%;background:#c8d1dc}
.dots span:first-child{background:var(--blue)}

/* section title */
.section-title{position:absolute;left:0;width:1200px;text-align:center}
.section-title h2{font-family:"Montserrat",sans-serif;font-weight:700;font-size:30px;color:var(--navy);letter-spacing:2px}
.section-title h2::after{content:"";display:block;width:40px;height:3px;background:var(--sky);margin:8px auto 6px}
.section-title p{font-size:11px;color:var(--muted)}

/* news */
.news-bg{position:absolute;top:540px;left:0;width:1200px;height:780px;background:linear-gradient(180deg,#fff,var(--pale))}
.news-tabs{position:absolute;top:680px;left:100px;width:1000px;display:flex;gap:4px}
.news-tabs span{flex:1;height:40px;line-height:40px;text-align:center;background:#e6eaef;font-size:12px}
.news-tabs span.active{background:var(--navy);color:#fff}
.news-list{position:absolute;top:736px;left:100px;width:1000px;list-style:none}
.news-list li{height:50px;display:flex;align-items:center;border-bottom:1px solid var(--line);font-size:12px;background:#fff}
.news-list time{width:110px;padding-left:16px;font-family:"Montserrat",sans-serif;color:#555}
.tag{width:74px;height:20px;line-height:20px;text-align:center;color:#fff;font-size:10px;margin-right:24px}
.tag.ir{background:#c7434a}.tag.info{background:var(--blue)}.tag.prod{background:#2aa1b8}
.more-btn{position:absolute;top:1226px;left:420px;width:360px;height:44px;border-radius:22px;background:var(--sky);color:#fff;text-align:center;line-height:44px;font-size:13px}

/* feature cards */
.cards{position:absolute;top:1360px;left:90px;width:1020px;display:flex;gap:20px}
.card{flex:1;height:180px;position:relative}
.card span{position:absolute;right:12px;bottom:14px;color:#fff;font-weight:700;font-size:15px;background:rgba(12,42,91,.78);padding:4px 12px}

/* products */
.product-grid{position:absolute;top:1720px;left:0;width:1200px;display:grid;grid-template-columns:320px 280px 260px 340px;grid-template-rows:260px 260px}
.cell-text{background:var(--dark);color:#fff;padding:34px 30px}
.cell-text.alt{background:var(--darker)}
.cell-text.light{background:#e9edf1;color:var(--text)}
.cell-text h3{font-size:19px;font-weight:700;margin-bottom:12px}
.cell-text p{font-size:11px;line-height:1.8;opacity:.85}
.cell-text .arrow{display:block;margin-top:18px;font-size:12px;color:var(--sky)}

/* banners */
.banners{position:absolute;top:2340px;left:100px;width:1000px;display:flex;gap:20px}
.banner{flex:1;height:240px;position:relative}
.banner .label{position:absolute;left:20px;top:22px;color:#fff;background:rgba(12,42,91,.78);padding:8px 16px}
.banner .label strong{display:block;font-size:20px;font-weight:700}
.banner .label small{display:block;font-size:11px;margin-top:2px;opacity:.9}

/* contact */
.contact{position:absolute;top:2640px;left:0;width:1200px;height:56px;background:var(--navy);display:flex;align-items:center;padding:0 40px;color:#fff}
.contact h2{font-family:"Montserrat",sans-serif;font-size:22px;letter-spacing:2px}
.contact small{font-size:10px;margin-left:10px;opacity:.8}
.contact p{margin-left:auto;font-size:11px;width:420px;line-height:1.6;opacity:.9}
.contact .btn{margin-left:20px;border:1px solid #fff;padding:7px 22px;font-size:12px}

/* footer */
.site-footer{position:absolute;top:2696px;left:0;width:1200px;height:384px;background:linear-gradient(90deg,#fff 50%,#dfe5ec 100%);padding:36px 40px;display:flex;gap:40px}
.footer-company{width:240px;font-size:11px;line-height:1.8}
.footer-company .brand{font-size:26px;display:block;margin-bottom:8px}
.footer-company .tel{display:inline-block;margin-top:8px;background:var(--sky);color:#fff;padding:3px 10px;font-size:10px}
.footer-col h4{font-size:12px;color:var(--navy);margin-bottom:6px}
.footer-col ul{list-style:none;font-size:10px;line-height:1.9;color:#555}
.copyright{position:absolute;top:3080px;left:0;width:1200px;height:40px;background:var(--navy);color:#fff;font-size:10px;display:flex;align-items:center;padding:0 40px;justify-content:space-between}
</style>
</head>
<body>

<header class="site-header">
  <span class="brand">HARUDEN</span>
  <div class="header-right">
    <div class="utility"><span class="search"></span><span>› メンバーログイン</span><span>› サイトマップ</span></div>
    <nav class="global-nav">
      <a>企業情報</a><a>IR情報</a><a>製品情報</a><a>販売ネットワーク</a><a>採用センター</a><a>採用情報</a><a>お問い合わせ</a>
    </nav>
  </div>
</header>

<section class="hero" role="img" aria-label="油圧ショベルが稼働する造成現場の写真">
  <div class="hero-copy">
    <h1>LIVING WITH HYDRAULIC</h1>
    <p>油圧に生きる</p>
  </div>
  <svg class="hero-arrow" style="left:20px" viewBox="0 0 20 30"><path d="M15 3 3 15l12 12" fill="none" stroke="#fff" stroke-width="2"/></svg>
  <svg class="hero-arrow" style="right:20px" viewBox="0 0 20 30"><path d="M5 3l12 12L5 27" fill="none" stroke="#fff" stroke-width="2"/></svg>
</section>
<div class="dots"><span></span><span></span><span></span><span></span><span></span><span></span><span></span><span></span><span></span></div>

<div class="news-bg"></div>
<div class="section-title" style="top:580px"><h2>NEWS</h2><p>最新情報</p></div>
<div class="news-tabs"><span class="active">すべて</span><span>お知らせ</span><span>製品ニュース</span><span>IRニュース</span></div>
<ul class="news-list">
  <li><time>2021.09.16</time><span class="tag ir">IR</span>第3四半期決算短信</li>
  <li><time>2021.07.01</time><span class="tag info">お知らせ</span>第77期定時株主総会決議ご通知</li>
  <li><time>2021.05.23</time><span class="tag info">お知らせ</span>当社株式の大規模買付行為への対応方針（買収防衛策）に関する一部改定のお知らせ</li>
  <li><time>2021.04.15</time><span class="tag prod">製品ニュース</span>新製品発売のお知らせ</li>
  <li><time>2021.04.03</time><span class="tag prod">製品ニュース</span>省エネ油圧ユニット</li>
  <li><time>2021.03.12</time><span class="tag info">お知らせ</span>当社株式の大規模買付行為への対応方針（買収防衛策）に関する一部改定のお知らせ</li>
  <li><time>2021.01.25</time><span class="tag ir">IR</span>役員の異動に関するお知らせ</li>
  <li><time>2021.01.08</time><span class="tag info">お知らせ</span>第77期定時株主総会招集ご通知</li>
</ul>
<a class="more-btn">一覧を見る</a>

<div class="cards">
  <div class="card" role="img" aria-label="本社ビルの外観写真" style="background:linear-gradient(160deg,#a9c6e6 0%,#6f93bd 55%,#3f6490 100%)"><span>会社案内</span></div>
  <div class="card" role="img" aria-label="工場内の製造ラインの写真" style="background:linear-gradient(160deg,#eef1f4 0%,#b9c1cb 60%,#8a95a3 100%)"><span>技術・品質</span></div>
  <div class="card" role="img" aria-label="会議中の社員の写真" style="background:linear-gradient(160deg,#d6dde5 0%,#8896a8 60%,#4f5e72 100%)"><span>IR情報</span></div>
  <div class="card" role="img" aria-label="販売ネットワークを示す地球のイメージ" style="background:linear-gradient(160deg,#6fb2e6 0%,#3f85cc 55%,#1b4f8f 100%)"><span>販売ネットワーク</span></div>
</div>

<div class="section-title" style="top:1620px"><h2>PRODUCT</h2><p>製品情報</p></div>
<div class="product-grid">
  <div role="img" aria-label="油圧ポンプの製品写真" style="background:radial-gradient(circle at 50% 50%,#9aa2ac 0%,#cfd4da 45%,#f4f5f7 100%)"></div>
  <div class="cell-text"><h3>油圧機器</h3><p>高性能な油圧ポンプ・バルブを幅広くご用意しています。用途に応じた最適な製品をお選びいただけます。</p><span class="arrow">› 詳しく見る</span></div>
  <div role="img" aria-label="油圧シリンダの製品写真" style="background:radial-gradient(circle at 50% 45%,#4c5561 0%,#2a2f36 55%,#15181c 100%)"></div>
  <div class="cell-text alt"><h3>油圧取扱情報</h3><p>製品の取扱説明書や技術資料をご覧いただけます。安全にご使用いただくための情報です。</p><span class="arrow">› 詳しく見る</span></div>
  <div class="cell-text alt"><h3>環境機器</h3><p>省エネと環境負荷の低減に貢献する機器をご紹介しています。</p><span class="arrow">› 詳しく見る</span></div>
  <div role="img" aria-label="青い環境機器の製品写真" style="background:radial-gradient(circle at 50% 50%,#7ab8ea 0%,#3f7fc6 50%,#1f4f96 100%)"></div>
  <div class="cell-text light"><h3>油圧セミナー</h3><p>基礎から応用まで、油圧技術を学べるセミナーを開催しています。</p><span class="arrow">› 詳しく見る</span></div>
  <div role="img" aria-label="セミナー会場の写真" style="background:radial-gradient(circle at 60% 40%,#5a6d8c 0%,#2a3a55 50%,#10192a 100%)"></div>
</div>

<div class="banners">
  <div class="banner" role="img" aria-label="並んで立つ社員の写真" style="background:linear-gradient(135deg,#9dbedf 0%,#5f86b2 55%,#2f4f78 100%)"><div class="label"><strong>採用情報</strong><small>新卒・中途採用情報</small></div></div>
  <div class="banner" role="img" aria-label="展示会ブースの写真" style="background:linear-gradient(135deg,#6a7b99 0%,#34425d 55%,#121c30 100%)"><div class="label"><strong>展示会</strong><small>出展スケジュール</small></div></div>
</div>

<section class="contact">
  <h2>CONTACT</h2><small>お問い合わせ</small>
  <p>製品に関するご質問、ご相談、カタログのご請求などお気軽にお問い合わせください。</p>
  <a class="btn">お問い合わせ</a>
</section>

<footer class="site-footer">
  <div class="footer-company">
    <span class="brand">HARUDEN</span>
    春電工業株式会社<br>〒105-0000<br>東京都港区芝浦0-0-0
    <br><span class="tel">TEL 03-0000-0000</span>
  </div>
  <div class="footer-col"><h4>企業情報</h4><ul><li>› 会社概要</li><li>› 沿革</li><li>› 事業所</li><li>› 品質方針</li><li>› 環境方針</li></ul></div>
  <div class="footer-col"><h4>IR情報</h4><ul><li>› IRニュース</li><li>› 決算情報</li><li>› 株式情報</li><li>› 株主総会</li></ul></div>
  <div class="footer-col"><h4>製品情報</h4><ul><li>› 油圧機器</li><li>› 環境機器</li><li>› 油圧セミナー</li><li>› 取扱情報</li></ul></div>
  <div class="footer-col"><h4>販売ネットワーク</h4><ul><li>› 国内販売網</li><li>› 海外販売網</li></ul><h4 style="margin-top:10px">採用センター</h4><ul><li>› 新卒採用</li></ul></div>
  <div class="footer-col"><h4>その他</h4><ul><li>› お問い合わせ</li><li>› サイトマップ</li><li>› プライバシー</li></ul></div>
</footer>
<div class="copyright"><span>ウェブサイトの利用条件　　個人情報保護方針</span><span class="en">2021 Copyright © HARUDEN KOGYO CO.,LTD. All rights reserved.</span></div>

</body>
</html>
```